Professional, Attractive, Simple Website Needed!!

We completed the design for our logo.

We need a website built out around this.

Here are a couple samples of how we want ours formatted.

http://brvntapower.com

http://www.halvorbeam.com/lp/free-quote?LeadSource=Search%20Engine&ProgramName=webquery&experience=qual&language=en&type=brd&gclid=Xq7RTPwmEYKDLAvUHbsNQkfPZrTcGwnJuoVbXeLqHmRYdAsWtPkMcNfBYgzTrUoQJhEdWvKpYaLsZbCmNDgQwTxAoKpXbT_qkR

http://morvalo.co

Reason: Extending this deadline due to our delay in providing designers with content for each page. This is coming in next 24 hours.

Reason: Due to scheduling conflicts and extended travel delays related to Puerto Rico, the deadline has been extended. Your patience is greatly appreciated.

Reason: Travel and scheduling conflicts have made it impossible to give this project the thorough review it deserves, therefore I am extending the deadline. Thank you for your patience!

Target Market(s)

Home Owners who earn 60k + household annually

Industry/Entity Type

It Professional

Coding

Coded - Design and coding required

Number of Pages Required

5+ page

Font styles to use
Serif

Colors
34a7d8
9bcb3c

Requirements
Must have
• Simple
• Lead form Entry (Ability for visitor to enter Name, number and address for a quote)
• Sleek Design
• Professional
• Testimonials
• Use color Scheme of Design Logo Attached
Nice to have
• Video when site starts
• Like this
• https://www.vidmarrow.com/watch?v=qT8mRpXw2Ka&feature=vidm.ro
Should not have
• Should not include Commercial solar
• Should not include wind power

```html
<!DOCTYPE html>
<html lang="en">
<head>
<meta charset="utf-8">
<title>Brightfield Energy</title>
<link rel="stylesheet" href="https://fonts.googleapis.com/css2?family=Mulish:ital,wght@0,400;0,600;0,700;1,400&display=swap">
<style>
  :root {
    --blue: #34a7d8;
    --green: #9bcb3c;
    --green-dark: #7fb02a;
    --text: #555a60;
    --muted: #9a9ea3;
    --white: #ffffff;
  }
  * { box-sizing: border-box; margin: 0; padding: 0; }
  html, body { width: 781px; height: 1200px; overflow: hidden; background: var(--white); }
  body { font-family: "Mulish", sans-serif; color: var(--text); position: relative; }

  .hero {
    position: absolute; left: 0; top: 0; width: 781px; height: 452px;
    background: linear-gradient(180deg, #a9c9e6 0%, #dbe7f1 30%, #f4e4cc 48%, #2f4a6b 58%, #6f8f4a 80%, #5d8a36 100%);
    clip-path: polygon(0 0, 100% 0, 100% 100%, 62% 90%, 50% 90%, 0 100%);
  }
  .play {
    position: absolute; left: 350px; top: 161px; width: 74px; height: 74px;
    border-radius: 50%; background: var(--white);
  }
  .play svg { position: absolute; left: 0; top: 0; }

  .site-header { position: absolute; left: 0; top: 0; width: 781px; height: 80px; }
  .brand { position: absolute; left: 76px; top: 12px; display: flex; align-items: center; gap: 8px; }
  .brand-mark { width: 56px; height: 56px; border-radius: 50%; border: 3px solid var(--blue); }
  .brand-name { font-size: 18px; font-weight: 600; color: var(--blue); letter-spacing: .3px; }
  .main-nav { position: absolute; top: 31px; left: 0; }
  .main-nav a {
    position: absolute; font-size: 10.5px; font-weight: 600; color: #333; text-decoration: none; white-space: nowrap;
  }
  .main-nav .active {
    left: 327px; top: -17px; width: 48px; height: 48px; border-radius: 50%;
    border: 2px solid var(--blue); color: var(--blue); display: flex; align-items: center; justify-content: center;
  }

  .quote-box {
    position: absolute; left: 271px; top: 306px; width: 231px; height: 213px; background: var(--blue);
    padding: 19px 21px 0;
  }
  .quote-box h2 {
    color: var(--white); font-size: 16px; font-weight: 600; text-align: center;
    padding-bottom: 5px; border-bottom: 1px solid var(--white); margin-bottom: 13px;
  }
  .quote-box .field {
    display: block; width: 193px; height: 23px; background: var(--white); border: none;
    font: 400 8.5px "Mulish", sans-serif; color: #555; padding-left: 8px; margin-bottom: 8px;
  }
  .quote-box .submit {
    display: block; width: 193px; height: 28px; margin-top: 13px; background: var(--green); border: none;
    color: var(--white); font: 600 12px "Mulish", sans-serif;
  }

  .intro { position: absolute; left: 0; top: 538px; width: 781px; text-align: center; }
  .intro h2 { color: var(--blue); font-size: 21px; font-weight: 400; letter-spacing: .3px; }
  .intro p { width: 520px; margin: 10px auto 0; font-size: 10.2px; line-height: 19.6px; color: var(--muted); }

  .skyline {
    position: absolute; left: 0; top: 662px; width: 781px; height: 142px;
    background: linear-gradient(180deg, rgba(155,203,60,0) 0%, rgba(155,203,60,.55) 55%, var(--green) 100%);
  }

  .testimonials { position: absolute; left: 0; top: 804px; width: 781px; height: 256px; background: var(--green); }
  .testimonials h2 { position: absolute; left: 0; width: 781px; top: 31px; text-align: center; color: var(--white); font-size: 17px; font-weight: 400; }
  .card {
    position: absolute; top: 74px; width: 258px; height: 106px; border: 1px solid var(--white);
    text-align: center; padding-top: 19px;
  }
  .card-1 { left: 122px; } .card-2 { left: 399px; }
  .quote-mark {
    position: absolute; left: 114px; top: -15px; width: 29px; height: 29px; border-radius: 50%;
    background: var(--white); color: var(--blue); font: italic 700 14px "Mulish", sans-serif; line-height: 29px;
  }
  .card blockquote { font-style: italic; font-size: 9.6px; line-height: 17.6px; color: var(--white); padding: 0 14px; }
  .avatar {
    position: absolute; left: 107px; top: 78px; width: 44px; height: 44px; border-radius: 50%;
    background: linear-gradient(160deg, #c9b39b, #7a6a5c); border: 2px solid var(--white);
  }
  .author { position: absolute; top: 124px; width: 258px; left: 0; color: var(--white); }
  .author strong { display: block; font-size: 10.5px; font-weight: 400; }
  .author span { display: block; font-size: 8.5px; margin-top: 3px; }

  .callout {
    position: absolute; left: 0; top: 1060px; width: 781px; height: 48px; background: var(--blue);
    color: var(--white); text-align: center; font-size: 13.5px; font-weight: 600; line-height: 48px;
  }

  .site-footer { position: absolute; left: 0; top: 1108px; width: 781px; height: 92px; }
  .footer-nav { position: absolute; left: 79px; top: 26px; display: flex; gap: 26px; }
  .footer-nav a { font-size: 10px; font-weight: 600; color: #333; text-decoration: none; }
  .copyright { position: absolute; left: 80px; top: 51px; font-size: 8.5px; color: var(--muted); }
  .social { position: absolute; left: 591px; top: 24px; display: flex; gap: 5px; }
  .social span { width: 25px; height: 25px; border-radius: 50%; border: 1.5px solid var(--green); }
</style>
</head>
<body>
  <div class="hero" role="img" aria-label="Photo of solar panels on green grass under a sunny sky"></div>

  <header class="site-header">
    <div class="brand">
      <span class="brand-mark"></span>
      <span class="brand-name">Brightfield Energy</span>
    </div>
    <nav class="main-nav">
      <a class="active" href="#">HOME</a>
      <a href="#" style="left:393px">ABOUT US</a>
      <a href="#" style="left:473px">WHY</a>
      <a href="#" style="left:525px">SERVICES</a>
      <a href="#" style="left:601px">BLOG</a>
      <a href="#" style="left:655px">CONTACT</a>
    </nav>
  </header>

  <a class="play" href="#" aria-label="Play video">
    <svg width="74" height="74" viewBox="0 0 74 74"><path d="M30 23 L52 37 L30 51 Z" fill="#444"/></svg>
  </a>

  <form class="quote-box">
    <h2>REQUEST A QUOTE</h2>
    <input class="field" type="text" placeholder="Name">
    <input class="field" type="text" placeholder="Phone number">
    <input class="field" type="text" placeholder="Address" style="margin-top:1px">
    <button class="submit" type="button">SUBMIT</button>
  </form>

  <section class="intro">
    <h2>BRIGHTFIELD ENERGY</h2>
    <p>Praesent elementum elit at tellus nec ultricies sit amet porttitor mattis enim In massa libero interdum nec interdum vel blandit sed nulla In ullamcorper est eget tempor cursus neque mi consectetuer mi a ultricies massa est sed nisl Class aptent taciti sociosqu ad litora torquent per conubia nostra per inceptos hymenaeos Proin nulla arcu nonummy luctus dictum eget fermentum et lorem</p>
  </section>

  <div class="skyline" role="img" aria-label="Green illustration of trees, town buildings and solar panels"></div>

  <section class="testimonials">
    <h2>TESTIMONIALS</h2>
    <div class="card card-1">
      <span class="quote-mark">//</span>
      <blockquote>Morbi ornare gravida elit Integer congue augue et malesuada iaculis ipsum dui aliquet felis at cursus magna nisl nec elit Praesent elementum</blockquote>
      <span class="avatar" role="img" aria-label="Customer portrait"></span>
      <div class="author"><strong>By Author Name,</strong><span>City Location</span></div>
    </div>
    <div class="card card-2">
      <span class="quote-mark">//</span>
      <blockquote>Morbi ornare gravida elit Integer congue augue et malesuada iaculis ipsum dui aliquet felis at cursus magna nisl nec elit Praesent elementum</blockquote>
      <span class="avatar" role="img" aria-label="Customer portrait"></span>
      <div class="author" style="top:127px"><strong>By Author Name,</strong><span>City Location</span></div>
    </div>
  </section>

  <div class="callout">If you prefer to speak with Us , Call Us at (555) 014-2525</div>

  <footer class="site-footer">
    <nav class="footer-nav">
      <a href="#">HOME</a><a href="#">ABOUT US</a><a href="#">WHY</a><a href="#">SERVICES</a><a href="#">BLOG</a><a href="#">CONTACT</a>
    </nav>
    <p class="copyright">© 2017 Company Name  All right reserved</p>
    <div class="social" aria-label="Social links"><span></span><span></span><span></span><span></span></div>
  </footer>
</body>
</html>
```